Car Detailing product label for 750ML Clear Bottle

I need a label for various product with differente color for each products but in the same size bottle each time. It's only for our purpose no commercial application. I need a template with differente color but same design. The name for product it's : Brisk Harbor. We dont have any logo because it's only for us. We like like car silhouette in the logo or in background or something like that.

And for the product we have many like : APC Cleaner, Drying Aid, Wheel Cleaner and some other.

Font styles to use
Serif
Sans Serif

```html
<!DOCTYPE html>
<html lang="en">
<head>
<meta charset="utf-8">
<title>Brisk Harbor – Wheel Cleaner Label</title>
<link rel="stylesheet" href="https://fonts.googleapis.com/css2?family=Archivo+Black&family=Teko:wght@400&family=Alfa+Slab+One&display=swap">
<style>
  :root {
    --backdrop: #474747;
    --label-white: #ffffff;
    --label-black: #121212;
    --brand-grey: #3b3b3b;
    --accent-teal: #3bb3c3;
    --text-light: #ffffff;
    --chrome-dark: #2a2a2a;
    --chrome-light: #f2f2f2;
  }
  html, body {
    margin: 0;
    padding: 0;
    width: 1200px;
    height: 1045px;
    overflow: hidden;
    background: var(--backdrop);
  }
  .label {
    position: absolute;
    left: 30px;
    top: 96px;
    width: 1140px;
    height: 852px;
    background: var(--label-black);
    overflow: hidden;
  }
  .label__top {
    position: absolute;
    left: 0; top: 0;
    width: 100%;
    height: 349px;
    background: var(--label-white);
  }
  .label__art {
    position: absolute;
    left: 0; top: 0;
    width: 1140px;
    height: 852px;
  }
  .brand-name {
    position: absolute;
    left: 0;
    width: 100%;
    top: 128px;
    text-align: center;
    font-family: "Archivo Black", sans-serif;
    font-size: 66px;
    line-height: 1;
    color: var(--brand-grey);
    letter-spacing: -1px;
  }
  .product-line {
    position: absolute;
    left: 344px;
    width: 452px;
    top: 548px;
    text-align: center;
    font-family: "Teko", sans-serif;
    font-weight: 400;
    font-size: 70px;
    line-height: 1;
    color: var(--text-light);
    font-variant: small-caps;
  }
  .product-box {
    position: absolute;
    left: 364px;
    top: 616px;
    width: 411px;
    height: 217px;
    background: var(--accent-teal);
    display: flex;
    flex-direction: column;
    align-items: center;
    justify-content: flex-start;
    padding-top: 38px;
    box-sizing: border-box;
  }
  .product-name {
    margin: 0;
    font-family: "Alfa Slab One", serif;
    font-weight: 400;
    font-size: 58px;
    line-height: 56px;
    color: var(--text-light);
    text-align: center;
    letter-spacing: 1px;
  }
  .volume {
    position: absolute;
    left: 940px;
    top: 740px;
    font-family: "Teko", sans-serif;
    font-size: 70px;
    line-height: 1;
    color: var(--text-light);
  }
</style>
</head>
<body>
  <div class="label">
    <div class="label__top"></div>

    <svg class="label__art" viewBox="0 0 1140 852" aria-hidden="false">
      <defs>
        <linearGradient id="chrome" x1="0" y1="0" x2="1" y2="0">
          <stop offset="0" stop-color="#3a3a3a"/>
          <stop offset="0.12" stop-color="#f4f4f4"/>
          <stop offset="0.25" stop-color="#8a8a8a"/>
          <stop offset="0.4" stop-color="#e8e8e8"/>
          <stop offset="0.55" stop-color="#6a6a6a"/>
          <stop offset="0.7" stop-color="#f0f0f0"/>
          <stop offset="0.85" stop-color="#9a9a9a"/>
          <stop offset="1" stop-color="#d8d8d8"/>
        </linearGradient>
        <linearGradient id="chrome-vertical" x1="0" y1="0" x2="0" y2="1">
          <stop offset="0" stop-color="#444"/>
          <stop offset="0.5" stop-color="#eeeeee"/>
          <stop offset="1" stop-color="#555"/>
        </linearGradient>
        <radialGradient id="mesh" cx="0.5" cy="0.45" r="0.6">
          <stop offset="0" stop-color="#6a6a6a"/>
          <stop offset="0.6" stop-color="#3a3a3a"/>
          <stop offset="1" stop-color="#1c1c1c"/>
        </radialGradient>
      </defs>

      <!-- chrome band under the white panel -->
      <rect class="band band--upper" x="0" y="349" width="1140" height="42" fill="url(#chrome)"/>
      <rect x="0" y="349" width="1140" height="3" fill="#2b2b2b"/>
      <!-- chrome band at the bottom edge -->
      <rect class="band band--lower" x="0" y="833" width="1140" height="19" fill="url(#chrome)"/>

      <!-- grille emblem -->
      <g class="emblem">
        <path d="M270 304 H870 Q900 304 888 330 L838 420 Q830 434 812 438 L570 492 L328 438 Q310 434 302 420 L252 330 Q240 304 270 304 Z"
              fill="#1a1a1a"/>
        <path d="M275 312 H865 Q888 312 878 332 L830 416 Q823 428 808 431 L570 484 L332 431 Q317 428 310 416 L262 332 Q252 312 275 312 Z"
              fill="url(#chrome)"/>
        <path d="M284 320 H856 Q874 320 866 336 L822 412 Q816 421 804 424 L570 474 L336 424 Q324 421 318 412 L274 336 Q266 320 284 320 Z"
              fill="url(#mesh)" role="img" aria-label="Metallic honeycomb grille mesh"/>
      </g>
    </svg>

    <div class="brand-name">Brisk Harbor</div>

    <div class="product-line">Cleaning &amp; Sanitizing</div>

    <div class="product-box">
      <h1 class="product-name">WHEEL<br>CLEANER</h1>
    </div>

    <div class="volume">750ML</div>
  </div>
</body>
</html>
```